Webdesign mit Wordpress DIVI Theme - CI und Logo vorhanden
Zielgruppe
Wir veranstalten eine Messe zum Thema Reinigung von Zügen und Straßenbahnen. Die Webseite soll folgende Zielgruppen ansprechen:
* Aussteller (Reinigungsindustrie)
* Besucher
* Presse
Aufgabenstellung
Wir brauchen ein Wordpress Deisgn basierend auf dem DIVI Theme!
Erwartet wird ein fertiges Layout mit Divi gemacht, welches wir importieren können.
Es gibt bereits einen Styleguide und ein Logo. Diese sind angehängt. Bitte entsprechend berücksichtigen.

```html
<!DOCTYPE html>
<html lang="de">
<head>
<meta charset="utf-8">
<title>railwash – Messe 2019</title>
<link href="https://fonts.googleapis.com/css2?family=Prompt:wght@300;400;500;600&display=swap" rel="stylesheet">
<style>
:root{
  --slate:#4b6b79;
  --heading:#3f6878;
  --brand:#1e5868;
  --gold:#e09a08;
  --mist:#d8e9f1;
  --ink:#1d2a33;
  --muted:#7f98a4;
  --white:#ffffff;
  --footer:#2a2d31;
}
*{margin:0;padding:0;box-sizing:border-box}
html,body{width:1200px;height:3795px;overflow:hidden;background:var(--white)}
body{position:relative;font-family:"Prompt",sans-serif;font-weight:300;color:var(--muted)}
.abs{position:absolute}
.photo{position:absolute}
.center{text-align:center}
.btn{position:absolute;display:inline-block;font-family:"Prompt",sans-serif;font-weight:500;font-size:10px;letter-spacing:.5px}
.btn-slate{background:var(--slate);color:var(--white);padding:5px 12px}
.btn-white{background:var(--white);color:var(--slate);padding:5px 14px}
.brand-word{font-family:"Prompt",sans-serif;font-weight:500;color:var(--white);letter-spacing:.5px}

/* header */
.site-header{position:absolute;left:0;top:0;width:1200px;height:47px;background:var(--white);z-index:3}
.logo-box{position:absolute;left:339px;top:0;width:97px;height:96px;background:var(--brand);z-index:4;display:flex;flex-direction:column;align-items:center;justify-content:center;gap:6px}
.logo-dot{width:18px;height:18px;border-radius:50%;background:var(--white)}
.logo-box .brand-word{font-size:17px}
.nav{position:absolute;left:715px;top:26px;display:flex;gap:19px;font-family:"Prompt",sans-serif;font-weight:600;font-size:7px;color:var(--ink);z-index:4}

/* hero */
.hero-title{left:0;top:212px;width:1200px;font-weight:600;font-size:22px;color:var(--white)}
.hero-text{left:385px;top:244px;width:430px;font-size:10px;line-height:15px;color:var(--white)}

/* intro */
.intro-title{left:0;top:594px;width:1200px;font-weight:500;font-size:26px;color:var(--heading)}
.intro-logo{left:0;top:650px;width:1200px;display:flex;flex-direction:column;align-items:center;gap:4px}
.intro-logo .logo-dot{background:var(--brand);width:16px;height:16px}
.intro-logo .brand-word{color:var(--brand);font-size:18px}
.intro-text{left:350px;top:721px;width:505px;font-size:9.5px;line-height:14.6px}

/* exhibitors */
.section-title-white{left:0;top:1014px;width:1200px;font-weight:600;font-size:31px;color:var(--white)}
.stat-card{left:339px;top:1088px;width:521px;height:298px;background:rgba(255,255,255,.9)}
.stat-ring{left:568px;top:1126px;width:64px;height:64px;border:2px solid #bccbd2;border-radius:50%;display:flex;align-items:center;justify-content:center;font-weight:500;font-size:19px;color:var(--slate)}
.stat-label{left:339px;top:1196px;width:521px;font-weight:500;font-size:13px;color:var(--heading)}
.stat-text{left:520px;top:1224px;width:160px;font-size:9.5px;line-height:14.6px}
.tile{position:absolute;color:var(--white);text-align:center}
.tile h3{font-weight:500;font-size:14px;line-height:15px}
.tile p{font-size:9px;line-height:15px;margin-top:6px}

/* visitors */
.visitor-title{left:209px;top:1830px;font-weight:500;font-size:26px;color:var(--heading)}
.visitor-text{left:209px;top:1866px;width:470px;font-size:9.5px;line-height:14.6px}
.ticket-box{left:730px;top:1835px;width:259px;height:96px;background:var(--mist)}
.ticket-box h2{position:absolute;left:0;top:16px;width:259px;text-align:center;font-weight:500;font-size:25px;color:var(--ink)}
.facts{left:600px;top:2020px;width:259px}
.facts h3{font-weight:500;font-size:13px;color:var(--heading)}
.facts p{font-size:9.5px;line-height:14.6px;margin:5px 30px 0}

/* contact */
.contact-logo{left:522px;top:2501px;width:150px;height:151px;background:var(--brand);display:flex;flex-direction:column;align-items:center;justify-content:center;gap:10px}
.contact-logo .logo-dot{width:26px;height:26px}
.contact-logo .brand-word{font-size:26px}
.contact-title{left:339px;top:2694px;font-weight:500;font-size:21px;color:var(--heading)}
.field{position:absolute;background:var(--white);font-size:8px;color:#5e6d75;padding:6px 8px}

/* press */
.press-title{left:0;top:3064px;width:1200px;font-weight:500;font-size:26px;color:var(--heading)}
.press-sub{left:128px;top:3136px;font-weight:500;font-size:10px;color:var(--heading)}
.press-text{left:128px;width:943px;font-size:7.6px;line-height:14.4px}
.accordion{position:absolute;left:119px;width:961px;height:28px;background:var(--mist);font-size:10px;color:var(--slate);padding:8px 10px}
.accordion::after{content:"";position:absolute;right:14px;top:11px;width:6px;height:6px;border-radius:50%;background:var(--slate)}

.site-footer{left:0;top:3762px;width:1200px;height:33px;background:var(--footer);font-size:7px;letter-spacing:1.5px;color:#7a7f85;padding-top:12px}
</style>
</head>
<body>

<header class="site-header">
  <nav class="nav"><span>AUSSTELLER</span><span>BESUCHER</span><span>PRESSE</span></nav>
</header>
<div class="logo-box"><span class="logo-dot"></span><span class="brand-word">railwash</span></div>

<!-- hero -->
<section class="hero">
  <div class="photo" role="img" aria-label="Foto: U-Bahnsteig mit Lichtspuren eines einfahrenden Zuges" style="left:0;top:47px;width:1200px;height:461px;background:linear-gradient(100deg,#4a4f55 0%,#8a8e92 30%,#2b2c30 55%,#5a4630 75%,#1a1a1c 100%)"></div>
  <svg class="abs" style="left:0;top:430px" width="1200" height="100" viewBox="0 0 1200 100">
    <path d="M0 55 Q600 40 1200 8 L1200 100 L0 100Z" fill="var(--gold)"/>
    <path d="M0 80 Q600 62 1200 52 L1200 100 L0 100Z" fill="var(--white)"/>
  </svg>
  <h1 class="abs center hero-title">Your Title Goes Here</h1>
  <p class="abs center hero-text">Your content goes here. Edit or remove this text inline or in the module Content settings. You can also style every aspect of this content in the module Design settings and even apply custom CSS to this text in the module Advanced settings.</p>
  <span class="btn btn-slate" style="left:560px;top:298px;letter-spacing:2px">Click Here</span>
</section>

<!-- intro -->
<section>
  <h2 class="abs center intro-title">Messe 2019</h2>
  <div class="abs intro-logo"><span class="logo-dot"></span><span class="brand-word">railwash</span></div>
  <p class="abs center intro-text">Lorem ipsum dolor sit amet, consetetur sadipscing elitr, sed diam nonumy eirmod tempor invidunt ut labore et dolore magna aliquyam erat, sed diam voluptua. At vero eos et accusam et justo duo dolores et ea rebum. Stet clita kasd gubergren, no sea takimata sanctus est Lorem ipsum dolor sit amet. Lorem ipsum dolor sit amet, consetetur sadipscing elitr, sed diam nonumy eirmod tempor invidunt ut labore et aliquyam erat, sed diam voluptua. At vero eos et accusam et justo duo dolores et ea rebum. Stet clita kasd gubergren, no sea takimata sanctus est Lorem ipsum dolor sit amet.</p>
</section>

<!-- exhibitors -->
<section>
  <svg class="abs" style="left:0;top:870px" width="1200" height="872" viewBox="0 0 1200 872" role="img" aria-label="Foto: blaue Stahlkonstruktion eines Bahnhofs und ein vorbeifahrender Zug">
    <defs>
      <linearGradient id="exhibitBg" x1="0" y1="0" x2="1" y2="1">
        <stop offset="0" stop-color="#1d4fb8"/>
        <stop offset=".45" stop-color="#c9d8ee"/>
        <stop offset=".7" stop-color="#2a4ea6"/>
        <stop offset="1" stop-color="#0c1f5e"/>
      </linearGradient>
    </defs>
    <path d="M0 50 Q600 40 1200 2 L1200 800 L0 870Z" fill="url(#exhibitBg)"/>
    <path d="M0 870 Q600 830 1200 780 L1200 815 Q700 850 0 872Z" fill="var(--gold)"/>
  </svg>
  <h2 class="abs center section-title-white">Aussteller Infos</h2>
  <div class="abs stat-card"></div>
  <div class="abs stat-ring">300</div>
  <div class="abs center stat-label">Aussteller</div>
  <p class="abs center stat-text">Lorem ipsum dolor sit amet, consetetur sadipscing elitr, sed diam nonumy eirmod invidunt ut labore et dolore magna aliquyam erat, sed diam voluptua. At vero eos et accusam et justo duo dolores et ea rebum</p>
  <span class="btn btn-slate" style="left:563px;top:1329px">Besucherliste</span>

  <div class="tile" style="left:339px;top:1397px;width:162px;height:155px;background:var(--slate);padding:20px 20px">
    <h3>Preise und Konditionen</h3>
    <p style="color:#c7d4da">Your content goes here. Edit or remove this text inline or in the module Content settings.</p>
  </div>
  <span class="btn btn-white" style="left:382px;top:1518px">mehr erfahren</span>

  <div class="tile" role="img" aria-label="Foto: Bahnsteig bei Nacht" style="left:517px;top:1386px;width:164px;height:262px;background:linear-gradient(180deg,#3b4150,#1c2230);padding:46px 16px">
    <h3 style="font-size:16px">Stand planen</h3>
    <p style="font-weight:500;font-size:8.5px;margin-top:4px">Wie Sie Ihren Stand richtig planen</p>
    <p style="color:#b8c0cc;margin-top:2px">Lorem ipsum dolor sit amet, consetetur sadipscing elitr, sed diam nonumy eirmod tempor invidunt, sed diam voluptua.</p>
  </div>
  <span class="btn btn-white" style="left:564px;top:1579px;letter-spacing:2px">Click Here</span>
  <svg class="abs" style="left:589px;top:1624px" width="22" height="6"><circle cx="3" cy="3" r="1.5" fill="#fff"/><circle cx="11" cy="3" r="1.5" fill="#fff"/><circle cx="19" cy="3" r="1.5" fill="#fff"/></svg>

  <div class="tile" role="img" aria-label="Foto: Wartebereich im Bahnhof" style="left:697px;top:1397px;width:162px;height:145px;background:linear-gradient(180deg,#1e2634,#0f151f);padding:18px 18px">
    <h3>Der richtige Stand</h3>
    <p style="color:#b8c0cc">Your content goes here. Edit or remove this text inline or in the module Content settings.</p>
  </div>
  <span class="btn btn-slate" style="left:738px;top:1507px">mehr erfahren</span>
</section>

<!-- visitors -->
<section>
  <h2 class="abs visitor-title">Besucher Infos</h2>
  <p class="abs visitor-text">Lorem ipsum dolor sit amet, consetetur sadipscing elitr, sed diam nonumy eirmod tempor invidunt ut labore et dolore magna aliquyam erat, sed diam voluptua. At vero eos et accusam et justo duo dolores et ea rebum. Stet clita kasd gubergren, no sea takimata sanctus est Lorem ipsum dolor sit amet. Lorem ipsum dolor sit amet, consetetur sadipscing elitr, sed diam nonumy eirmod tempor invidunt ut labore et aliquyam erat, sed diam voluptua. At vero eos et accusam et justo duo dolores et ea rebum. Stet clita kasd gubergren, no sea takimata sanctus est Lorem ipsum dolor sit amet.</p>
  <div class="abs ticket-box"><h2>Tickets kaufen</h2></div>
  <span class="btn btn-white" style="left:815px;top:1893px;font-weight:400;font-size:9px">zum Ticket-Shop</span>

  <div class="tile" role="img" aria-label="Foto: beleuchteter U-Bahnsteig" style="left:339px;top:2002px;width:261px;height:212px;background:linear-gradient(180deg,#2a2e36,#12161c);padding:38px 36px">
    <h3 style="font-weight:600;font-size:21px;line-height:22px">Unterkunft finden</h3>
    <p style="color:#c9ced4;font-size:9.5px;margin-top:8px">Kurze Beschreibung der Firma Lorem ipsum dolor sit amet, consetetur sadipscing elitr, sed diam nonumy eirmod tempor invidunt, sed diam voluptua.</p>
  </div>
  <span class="btn btn-slate" style="left:439px;top:2159px">Click Here</span>
  <svg class="abs" style="left:459px;top:2188px" width="20" height="6"><circle cx="3" cy="3" r="1.5" fill="#fff"/><circle cx="10" cy="3" r="1.5" fill="#fff"/><circle cx="17" cy="3" r="1.5" fill="#fff"/></svg>

  <div class="tile" style="left:339px;top:2214px;width:261px;height:118px;background:var(--slate);padding:20px 24px">
    <h3 style="font-size:13px">Gastronomie</h3>
    <p style="color:#c7d4da;margin-top:4px">Lorem ipsum dolor sit amet, consetetur sadipscing elitr, sed diam nonumy temporit ut labore ett.</p>
  </div>
  <span class="btn btn-white" style="left:428px;top:2291px">mehr erfahren</span>

  <div class="abs center facts">
    <h3>Daten &amp; Fakten</h3>
    <p>Your content goes here. Edit or remove this text inline or in the module Content settings.</p>
  </div>
  <span class="btn btn-slate" style="left:686px;top:2079px">mehr erfahren</span>

  <div class="photo" role="img" aria-label="Foto: Gleise an einem Bahnsteig" style="left:600px;top:2120px;width:259px;height:154px;background:linear-gradient(180deg,#3a3e42,#5b5f63 60%,#26292c)"></div>
  <div class="abs center" style="left:600px;top:2164px;width:259px;font-weight:500;font-size:21px;color:var(--gold)">Geländeplan</div>
  <span class="btn btn-slate" style="left:686px;top:2205px">mehr erfahren</span>
</section>

<!-- contact -->
<section>
  <svg class="abs" style="left:0;top:2436px" width="1200" height="568" viewBox="0 0 1200 568">
    <path d="M0 0 L1200 0 L1200 2 Q600 10 0 40Z" fill="var(--slate)"/>
    <path d="M0 40 Q600 10 1200 2 L1200 520 Q600 540 0 556Z" fill="var(--mist)"/>
    <path d="M0 556 Q600 540 1200 520 L1200 555 Q600 560 0 568Z" fill="var(--gold)"/>
  </svg>
  <div class="abs contact-logo"><span class="logo-dot"></span><span class="brand-word">railwash</span></div>
  <h2 class="abs contact-title">Kontakt &amp; Beratung</h2>
  <div class="field" style="left:339px;top:2727px;width:252px;height:23px">Name</div>
  <div class="field" style="left:607px;top:2727px;width:252px;height:23px">Vorname</div>
  <div class="field" style="left:339px;top:2768px;width:252px;height:24px">Telefonnummer</div>
  <div class="field" style="left:607px;top:2768px;width:252px;height:24px">E-Mail-Adresse</div>
  <div class="field" style="left:339px;top:2810px;width:520px;height:72px">Nachricht</div>
  <div class="abs" style="left:732px;top:2898px;font-size:9px;color:#7a8a92">6 + 3 =</div>
  <div class="abs" style="left:761px;top:2893px;width:24px;height:22px;background:var(--white)"></div>
  <span class="btn btn-slate" style="left:795px;top:2893px;padding:5px 10px;font-size:10px;height:22px">absenden</span>
</section>

<!-- press -->
<section>
  <h2 class="abs center press-title">Presse</h2>
  <h3 class="abs press-sub">Messe-Katalog</h3>
  <p class="abs press-text" style="top:3156px">Sed ut perspiciatis unde omnis iste natus error sit voluptatem accusantium doloremque laudantium, totam rem aperiam, eaque ipsa quae ab illo inventore veritatis et quasi architecto beatae vitae dicta sunt explicabo. Nemo enim ipsam voluptatem quia voluptas sit aspernatur aut odit aut fugit, sed quia consequuntur magni dolores eos qui ratione voluptatem sequi nesciunt. Neque porro quisquam est, qui dolorem ipsum quia dolor sit amet, consectetur, adipisci velit, sed quia non numquam eius modi tempora incidunt ut labore et dolore magnam aliquam quaerat voluptatem. Ut enim ad minima veniam, quis nostrum exercitationem ullam corporis suscipit laboriosam, nisi ut aliquid ex ea commodi consequatur? Quis autem vel eum iure reprehenderit qui in ea voluptate velit esse quam nihil molestiae consequatur, vel illum qui dolorem eum fugiat quo voluptas nulla pariatur?</p>
  <p class="abs press-text" style="top:3222px">At vero eos et accusamus et iusto odio dignissimos ducimus qui blanditiis praesentium voluptatum deleniti atque corrupti quos dolores et quas molestias excepturi sint occaecati cupiditate non provident, similique sunt in culpa qui officia deserunt mollitia animi, id est laborum et dolorum fuga. Et harum quidem rerum facilis est et expedita distinctio. Nam libero tempore, cum soluta nobis est eligendi optio cumque nihil impedit quo minus id quod maxime placeat facere possimus, omnis voluptas assumenda est, omnis dolor repellendus. Temporibus autem quibusdam et aut officiis debitis aut rerum necessitatibus saepe eveniet ut et voluptates repudiandae sint et molestiae non recusandae. Itaque earum rerum hic tenetur a sapiente delectus, ut aut reiciendis voluptatibus maiores alias consequatur aut perferendis doloribus asperiores repellat.</p>
  <div class="accordion" style="top:3320px">Messe-Katalog</div>
  <div class="accordion" style="top:3376px">Messe-Katalog</div>
  <div class="accordion" style="top:3432px">Messe-Katalog</div>
</section>

<!-- location -->
<div class="photo" role="img" aria-label="Karte: Umgebung des Messegeländes der Nordhallen Messe GmbH" style="left:0;top:3540px;width:1200px;height:222px;background:linear-gradient(135deg,#e8ebe6,#dde3dc 50%,#e9ebe8)"></div>
<svg class="abs" style="left:591px;top:3634px" width="16" height="22" viewBox="0 0 16 22"><path d="M8 22 C8 22 0 12 0 8 A8 8 0 0 1 16 8 C16 12 8 22 8 22Z" fill="#d93a2f"/><circle cx="8" cy="8" r="3" fill="#fff"/></svg>

<footer class="abs center site-footer">DATENSCHUTZERKLÄRUNG &nbsp;|&nbsp; IMPRESSUM</footer>

</body>
</html>
```